Real eatate

My company name is “Maple Crest Realestate” i would like to create a business card. I would like something modern and sleek similar to picture uploaded. All text in the business card should be black and the logo gold any shade.

```html
<!DOCTYPE html>
<html lang="en">
<head>
<meta charset="utf-8">
<title>Maple Crest Realestate – Business Card</title>
<link rel="stylesheet" href="https://fonts.googleapis.com/css2?family=Cinzel:wght@400;600&family=Crimson+Text:wght@400;600&display=swap">
<style>
  :root {
    --stage: #1c1c1e;
    --card-black: #070707;
    --card-white: #ffffff;
    --ink: #111111;
    --gold-dark: #a9822f;
    --gold-mid: #d7bd6c;
    --gold-light: #ecd98f;
    --divider: #1e2435;
  }
  * { box-sizing: border-box; margin: 0; padding: 0; }
  html, body {
    width: 1200px; height: 1189px; overflow: hidden;
    background: var(--stage);
  }
  .sheet {
    position: relative; width: 1200px; height: 1189px;
  }
  .card {
    position: absolute; left: 150px; width: 900px; height: 514px;
    border-radius: 34px; overflow: hidden;
    box-shadow: 0 18px 40px rgba(0,0,0,.55);
  }
  .card--front { top: 48px; background: var(--card-black); }
  .card--back  { top: 626px; background: var(--card-white); }

  /* brand name set as plain text */
  .brand {
    position: absolute; display: flex; align-items: center; gap: 22px;
    font-family: "Cinzel", serif; font-weight: 600;
  }
  .brand__dot {
    width: 44px; height: 44px; border-radius: 50%;
    background: var(--gold-mid); flex: none;
  }
  .brand__text { display: flex; flex-direction: column; align-items: center; line-height: 1.1; }
  .brand__name { font-size: 50px; letter-spacing: 2px; }
  .brand__tag  { font-size: 24px; letter-spacing: 7px; }

  .card--front .brand {
    left: 50%; top: 50%; transform: translate(-50%, -50%);
    color: var(--gold-mid);
  }
  .card--back .brand {
    left: 50px; top: 150px; color: var(--ink);
  }
  .card--back .brand__name { font-size: 42px; }
  .card--back .brand__tag  { font-size: 20px; letter-spacing: 6px; }
  .card--back .brand__dot  { width: 38px; height: 38px; }

  .divider {
    position: absolute; left: 470px; top: 70px; width: 2px; height: 250px;
    background: linear-gradient(to bottom, transparent, var(--divider) 15%, var(--divider) 85%, transparent);
  }

  .contact {
    position: absolute; left: 510px; top: 78px; color: var(--ink);
    font-family: "Crimson Text", serif;
  }
  .contact__name {
    font-family: "Cinzel", serif; font-weight: 600; font-size: 34px; line-height: 1;
  }
  .contact__role { font-size: 22px; margin-top: 2px; }
  .contact__address { font-size: 22px; line-height: 1.15; margin-top: 20px; }
  .contact__list { list-style: none; margin-top: 14px; }
  .contact__item {
    display: flex; align-items: center; gap: 12px;
    font-size: 23px; line-height: 1.5;
  }
  .contact__icon {
    width: 24px; height: 24px; border-radius: 50%; flex: none;
    background: radial-gradient(circle at 35% 30%, var(--gold-light), var(--gold-dark));
    display: flex; align-items: center; justify-content: center;
  }
  .contact__icon svg { width: 13px; height: 13px; }

  .band {
    position: absolute; left: 0; right: 0; top: 388px; height: 70px;
    background: linear-gradient(90deg, var(--gold-dark), var(--gold-mid) 35%, var(--gold-light) 55%, var(--gold-mid) 75%, var(--gold-dark));
    display: flex; align-items: center; justify-content: center;
    border-bottom: 4px solid #fff;
    box-shadow: 0 8px 0 var(--gold-dark);
  }
  .band__web {
    font-family: "Crimson Text", serif; font-size: 25px;
    letter-spacing: 9px; color: var(--ink);
  }
</style>
</head>
<body>
<main class="sheet">

  <section class="card card--front" aria-label="Card front">
    <div class="brand">
      <span class="brand__dot"></span>
      <div class="brand__text">
        <span class="brand__name">Maple Crest</span>
        <span class="brand__tag">– Realestate –</span>
      </div>
    </div>
  </section>

  <section class="card card--back" aria-label="Card back">
    <div class="brand">
      <span class="brand__dot"></span>
      <div class="brand__text">
        <span class="brand__name">Maple Crest</span>
        <span class="brand__tag">– Realestate –</span>
      </div>
    </div>

    <div class="divider"></div>

    <div class="contact">
      <p class="contact__name">Daniel Hart</p>
      <p class="contact__role">Executive Director</p>
      <p class="contact__address">PO Box 48 Harbor Lane<br>Portland, USA</p>
      <ul class="contact__list">
        <li class="contact__item">
          <span class="contact__icon"><svg viewBox="0 0 16 16"><path fill="#111" d="M4 1.5l2.5 3-1.5 1.7c.8 1.7 2.1 3 3.8 3.8l1.7-1.5 3 2.5-1.5 2.5C6.8 13.3 2.7 9.2 1.5 3z"/></svg></span>
          555-210-4817
        </li>
        <li class="contact__item">
          <span class="contact__icon"><svg viewBox="0 0 16 16"><rect x="3" y="3" width="10" height="10" rx="1.5" fill="none" stroke="#111" stroke-width="2"/></svg></span>
          555-210-4818
        </li>
        <li class="contact__item">
          <span class="contact__icon"><svg viewBox="0 0 16 16"><rect x="1.5" y="3.5" width="13" height="9" fill="#111"/><path d="M1.5 3.5L8 9l6.5-5.5" fill="none" stroke="#d7bd6c" stroke-width="1.2"/></svg></span>
          info@maplecrest.com
        </li>
      </ul>
    </div>

    <div class="band">
      <span class="band__web">www.maplecrestrealty.com</span>
    </div>
  </section>

</main>
</body>
</html>
```